Tarrow Consulting Needs Standardised Stationery!

Hello,I am looking at having some standardised stationery to continue building my brand. I am looking for a relatively clean and simple designs using the colours from my logos. Tarrow Consulting is the main business with Career Beacon Australia a subsidiary.
In particular I am after a design for:
- Letterhead (very important), white background, professional, corporate that I can send to prospective clients. Logo colours.
- Envelope, standard design I can print onto envelopes.
- Pens
- Other stationery/promotional items I can create

Target Market(s)

Universities, government, large organisations.

Industry/Entity Type

Professional Service

Font styles to use
Serif

Requirements
Must have
• Logo, match the design of the Tarrow Consulting logo. Black Career Beacon Australia logo is a subsidiary.
Should not have
• Too much colour, some colour is good, but I am looking for a clean professional look.

```html
<!DOCTYPE html>
<html lang="en">
<head>
<meta charset="utf-8">
<title>Tarrow Consulting Letterhead</title>
<link href="https://fonts.googleapis.com/css2?family=Lato:wght@400;700&family=Yellowtail&display=swap" rel="stylesheet">
<style>
  :root {
    --backdrop: #dcdcdc;
    --paper: #ffffff;
    --paper-shade: #f1f1f3;
    --ink: #4a4a4a;
    --ink-dark: #222222;
    --brand-blue: #1b8fc8;
    --brand-green: #2aa54a;
    --band-orange: #e8612c;
    --band-gold: #d89a32;
    --band-lime: #b3cd34;
    --band-blue: #22bbe8;
  }
  * { margin: 0; padding: 0; box-sizing: border-box; }
  html, body {
    width: 1200px; height: 1113px; overflow: hidden;
    background: var(--backdrop);
  }
  .letterhead {
    position: absolute; left: 220px; top: 30px;
    width: 760px; height: 1053px;
    background: linear-gradient(160deg, var(--paper) 35%, var(--paper-shade) 100%);
    font-family: "Lato", sans-serif;
    color: var(--ink);
  }
  .brand {
    position: absolute; left: 64px; top: 56px;
    display: flex; align-items: center; gap: 12px;
  }
  .brand-square { width: 26px; height: 26px; background: var(--ink-dark); }
  .brand-name {
    font-size: 24px; font-weight: 700; letter-spacing: 2px;
    color: var(--ink-dark);
  }
  .address {
    position: absolute; left: 560px; top: 53px;
    padding-left: 8px; border-left: 1px solid #bdbdbd;
    font-size: 11.5px; line-height: 16px; color: var(--ink);
  }
  .salutation {
    position: absolute; left: 64px; top: 236px;
    font-size: 14.5px; font-weight: 700; color: var(--brand-blue);
  }
  .body-copy {
    position: absolute; left: 64px; top: 276px; width: 631px;
  }
  .body-copy p {
    font-size: 14.6px; line-height: 24px; text-align: justify;
    hyphens: auto; margin-bottom: 17px;
  }
  .closing {
    position: absolute; left: 64px; top: 700px;
    font-size: 18px; color: var(--ink-dark);
  }
  .signature {
    position: absolute; left: 64px; top: 730px;
    font-family: "Yellowtail", cursive;
    font-size: 32px; color: var(--brand-blue);
  }
  .contacts {
    position: absolute; left: 64px; top: 966px;
    list-style: none; font-size: 11.5px; line-height: 18px;
  }
  .contacts li { display: flex; align-items: center; gap: 5px; }
  .contacts svg { width: 9px; height: 9px; fill: var(--brand-green); }
  .subsidiary {
    position: absolute; left: 610px; top: 980px;
    display: flex; align-items: center; gap: 7px;
  }
  .subsidiary-dot { width: 26px; height: 26px; border-radius: 50%; background: var(--ink-dark); }
  .subsidiary-name {
    width: 60px; font-size: 10px; line-height: 12px; font-weight: 700;
    color: var(--ink-dark);
  }
  .band { position: absolute; left: 0; bottom: 3px; width: 760px; height: 19px; display: block; }
</style>
</head>
<body>
  <main class="letterhead">
    <header>
      <div class="brand">
        <span class="brand-square"></span>
        <span class="brand-name">TARROW CONSULTING</span>
      </div>
      <address class="address" style="font-style:normal">
        Street Name, City Name<br>Zicode - 012345
      </address>
    </header>

    <p class="salutation">Dear Mr. Lorem,</p>

    <section class="body-copy">
      <p>Lorem ipsum dolor sit amet, consectetuer adipiscing elit, sed diam nonummy nibh euismod tincidunt ut laoreet dolore magna aliquam erat volutpat. Ut wisi enim ad minim veniam, quis nostrud exerci tation ullamcorper suscipit lobortis nisl ut aliquip ex ea commodo consequat. Duis autem vel eum iriure dolor in hendiusto odio dignissim qui blandit praesent luptatum zzril delenit augue duis dolore te feugait nulla facilisi.</p>
      <p>Lorem ipsum dolor sit amet, consectetuer adipiscing elit, sed diam nonummy nibh euismod tincidunt ut laoreet dolore magna aliquam erat volutpat. Ut wisi enim ad minim veniam, quis nostrud exerci tation ullamcorper suscipit lobortis nisl ut aliquip ex ea commodo consequat. Duis autem vel eum iriure dolor in hendiusto odio dignissim qui blandit praesent luptatum zzril delenit augue duis dolore te feugait nulla facilisi.</p>
      <p>Lorem ipsum dolor sit amet, consectetuer adipiscing elit, sed diam nonummy nibh euismod tincidunt ut laoreet dolore magna aliquam erat volutpat. Ut wisi enim ad minim veniam, quis nostrud exerci tation ullamcorper suscipit lobortis nisl ut aliquip ex ea commodo consequat. Duis autem vel eum iriure dolor in hendiusto odio dignissim qui blandit praesent luptatum zzril delenit augue duis dolore te feugait nulla facilisi.</p>
    </section>

    <p class="closing">Sincerely Your,</p>
    <p class="signature">Your Name</p>

    <footer>
      <ul class="contacts">
        <li><svg viewBox="0 0 10 10"><path d="M2 0.5 L3.6 2.6 L2.7 3.6 Q4 6 6.4 7.3 L7.4 6.4 L9.5 8 L8.2 9.6 Q3.5 9 0.4 1.8 Z"/></svg>012-345-6789</li>
        <li><svg viewBox="0 0 10 10"><path d="M0 2 H10 V8.5 H0 Z" /><path d="M0 2 L5 5.6 L10 2" fill="none" stroke="#fff" stroke-width="0.9"/></svg>sales@tarrowconsulting.com</li>
        <li><svg viewBox="0 0 10 10"><circle cx="5" cy="5" r="4.3" fill="none" stroke="var(--brand-green)" stroke-width="1"/><ellipse cx="5" cy="5" rx="1.8" ry="4.3" fill="none" stroke="var(--brand-green)" stroke-width="0.8"/><path d="M0.7 5 H9.3" stroke="var(--brand-green)" stroke-width="0.8"/></svg>www.tarrowconsulting.com</li>
      </ul>
      <div class="subsidiary">
        <span class="subsidiary-dot"></span>
        <span class="subsidiary-name">Career Beacon Australia</span>
      </div>
      <svg class="band" viewBox="0 0 760 19" preserveAspectRatio="none" aria-hidden="true">
        <defs>
          <linearGradient id="bandWarm" x1="0" x2="1" y1="0" y2="0">
            <stop offset="0" stop-color="var(--band-orange)"/>
            <stop offset="0.5" stop-color="var(--band-gold)"/>
            <stop offset="1" stop-color="var(--band-lime)"/>
          </linearGradient>
        </defs>
        <polygon points="0,0 394,0 376,19 0,19" fill="url(#bandWarm)"/>
        <polygon points="406,0 760,0 760,19 388,19" fill="var(--band-blue)"/>
      </svg>
    </footer>
  </main>
</body>
</html>
```